Kelvo Tech Oz Business card revamp

We are looking to revamp our business card design. We are hoping to change our colours to dark navey blue, gray, white and black but are open to keeping the same if a good design is submited. We are after somthing a bit differnt not just boring business card. I have attached a copy of our current card. We Want to keep the same logo design which i have attached a few to hopfully help you in this process. We are after a design that can be personalized to separate 4 people

Colors
0455a3
ffffff
000000
cbcbcb

Requirements
Must have
• Kelvo Tech Logo, address 3/41 Mallory Court, Wexhill 4218, phone number, Name and position

```html
<!DOCTYPE html>
<html lang="en">
<head>
<meta charset="utf-8">
<title>Kelvo Tech – Business Card</title>
<link href="https://fonts.googleapis.com/css2?family=Mulish:wght@400;600;800&display=swap" rel="stylesheet">
<style>
  :root{
    --stage:#2a2b2d;
    --brand-blue:#2f7fc4;
    --brand-blue-deep:#2a74b6;
    --accent-orange:#f07528;
    --ink:#3d3d3d;
    --paper:#ffffff;
  }
  *{margin:0;padding:0;box-sizing:border-box}
  html,body{width:1200px;height:900px;overflow:hidden;background:var(--stage);font-family:"Mulish",sans-serif}
  .stage{position:relative;width:1200px;height:900px}
  .card{position:absolute;left:250px;width:700px;height:400px;overflow:hidden;box-shadow:0 12px 30px rgba(0,0,0,.45)}
  .card--back{top:30px;background:linear-gradient(120deg,var(--brand-blue-deep),#3a8ad0)}
  .card--front{top:470px;background:var(--paper)}

  .wordmark{display:flex;align-items:center;gap:10px;font-weight:800;letter-spacing:.5px}
  .wordmark__dot{width:26px;height:26px;border-radius:50%}
  .card--back .wordmark{position:absolute;left:48px;bottom:70px;color:var(--paper);font-size:34px}
  .card--back .wordmark__dot{background:var(--accent-orange)}
  .card--back .mark-area{position:absolute;right:60px;top:70px;width:260px;height:240px;border-radius:50%;
    background:radial-gradient(circle,rgba(40,100,170,.45),rgba(40,100,170,0) 70%)}

  .card--front .wordmark{position:absolute;left:40px;top:40px;color:var(--brand-blue);font-size:32px}
  .card--front .wordmark__dot{background:var(--accent-orange)}
  .person{position:absolute;left:58px;top:118px}
  .person__name{color:var(--brand-blue);font-weight:600;font-size:22px;letter-spacing:.5px}
  .person__role{color:var(--ink);font-size:16px;font-weight:600;margin-top:0}
  .person__rule{width:16px;height:2px;background:var(--accent-orange);margin-top:10px}
  .contacts{position:absolute;left:58px;top:205px;list-style:none;color:var(--ink);font-size:17px;line-height:26px}
  .contacts li{display:flex;align-items:center;gap:14px}
  .contacts svg{width:14px;height:14px;fill:var(--accent-orange);flex:none}
  .contacts .web-domain{color:var(--brand-blue)}
  .address{position:absolute;left:58px;top:295px;color:var(--ink);font-size:17px;line-height:26px}
  .card--front .mark-area{position:absolute;right:50px;top:60px;width:280px;height:270px;border-radius:50%;
    background:radial-gradient(circle at 60% 45%,rgba(240,117,40,.35),rgba(47,127,196,.25) 55%,rgba(255,255,255,0) 72%)}
  .base-band{position:absolute;left:0;bottom:0;width:700px;height:16px}
</style>
</head>
<body>
<main class="stage">
  <section class="card card--back" aria-label="Card back">
    <div class="mark-area" role="img" aria-label="Faint brand symbol decoration"></div>
    <div class="wordmark"><span class="wordmark__dot"></span>Kelvo Tech</div>
  </section>

  <section class="card card--front" aria-label="Card front">
    <div class="wordmark"><span class="wordmark__dot"></span>Kelvo Tech</div>
    <div class="person">
      <p class="person__name">DANIEL ROURKE</p>
      <p class="person__role">Founder</p>
      <div class="person__rule"></div>
    </div>
    <ul class="contacts">
      <li><svg viewBox="0 0 24 24"><path d="M6.6 10.8a15 15 0 0 0 6.6 6.6l2.2-2.2c.3-.3.7-.4 1-.2 1.1.4 2.3.6 3.6.6.6 0 1 .4 1 1V20c0 .6-.4 1-1 1A17 17 0 0 1 3 4c0-.6.4-1 1-1h3.5c.6 0 1 .4 1 1 0 1.3.2 2.5.6 3.6.1.3 0 .7-.2 1z"/></svg>0491 570 316</li>
      <li><svg viewBox="0 0 24 24"><path d="M2 5h20v14H2zm2 2v.5l8 5 8-5V7l-8 5z"/></svg>info@kelvotech.com</li>
      <li><svg viewBox="0 0 24 24"><path d="M12 2a10 10 0 1 0 0 20 10 10 0 0 0 0-20zm6.9 6h-3a15 15 0 0 0-1.3-3.9A8 8 0 0 1 18.9 8zM12 4c.8 1.2 1.5 2.5 1.9 4h-3.8c.4-1.5 1.1-2.8 1.9-4zM4.3 14a8 8 0 0 1 0-4h3.4a16 16 0 0 0 0 4zm.8 2h3a15 15 0 0 0 1.3 3.9A8 8 0 0 1 5.1 16zm3-8h-3a8 8 0 0 1 4.3-3.9C8.8 5.3 8.4 6.6 8.1 8zM12 20c-.8-1.2-1.5-2.5-1.9-4h3.8c-.4 1.5-1.1 2.8-1.9 4zm2.3-6H9.7a14 14 0 0 1 0-4h4.6a14 14 0 0 1 0 4zm.3 5.9c.6-1.2 1-2.5 1.3-3.9h3a8 8 0 0 1-4.3 3.9zm1.7-5.9a16 16 0 0 0 0-4h3.4a8 8 0 0 1 0 4z"/></svg><span>www.<span class="web-domain">kelvotech.com</span>.au</span></li>
    </ul>
    <p class="address">PO Box 7182 Northgate<br>Wexhill WA 6091</p>
    <div class="mark-area" role="img" aria-label="Large brand symbol decoration"></div>
    <svg class="base-band" viewBox="0 0 700 16" preserveAspectRatio="none" aria-hidden="true">
      <polygon points="0,0 420,0 410,16 0,16" fill="var(--brand-blue)"/>
      <polygon points="428,0 700,0 700,16 418,16" fill="var(--accent-orange)"/>
    </svg>
  </section>
</main>
</body>
</html>
```